PWR Business Card

Looking for a business card for my restaurant group I own. Four different concepts:

Copperleaf Alehouse
Bramble Alehouse
Hollister's Wood Fired Grill
Fenwick Patty Company

Card doesn't need to include all the logos.

```html
<!DOCTYPE html>
<html lang="en">
<head>
<meta charset="utf-8">
<title>PWR Business Card</title>
<link rel="stylesheet" href="https://fonts.googleapis.com/css2?family=Lato:wght@400;700&family=Open+Sans:wght@400;600;700&display=swap">
<style>
  :root {
    --backdrop: #8a4a1c;
    --card-gold: #d3af6e;
    --card-dark: #1f1f1f;
    --ink: #111111;
    --rule-dark: #5a4a2e;
    --brand-gold: #cfae6c;
    --muted-light: #c9c9c9;
    --rule-light: #8c8c8c;
  }
  * { margin: 0; padding: 0; box-sizing: border-box; }
  html, body { width: 1200px; height: 900px; overflow: hidden; }
  body { background: var(--backdrop); position: relative; }

  .card {
    position: absolute;
    width: 556px;
    height: 343px;
    box-shadow: 3px 4px 8px rgba(0,0,0,0.45);
    display: flex;
    flex-direction: column;
    align-items: center;
    text-align: center;
  }

  /* Front: contact side */
  .card--contact {
    left: 330px; top: 90px;
    background: var(--card-gold);
    color: var(--ink);
    font-family: "Open Sans", sans-serif;
    padding-top: 64px;
  }
  .contact__name { font-weight: 700; font-size: 20px; line-height: 22px; letter-spacing: 0.2px; }
  .contact__title { font-size: 15px; line-height: 18px; }
  .contact__rule { width: 196px; height: 1px; background: var(--rule-dark); margin: 11px 0 12px; }
  .contact__lines { font-size: 16px; line-height: 20px; }
  .contact__lines b { font-weight: 700; }
  .contact__rule--lower { margin: 12px 0 16px; }
  .contact__address { font-size: 16px; line-height: 20px; }

  /* Back: brand side */
  .card--brand {
    left: 330px; top: 469px;
    width: 560px;
    background: var(--card-dark);
    font-family: "Lato", sans-serif;
    padding-top: 72px;
  }
  .brand__mark {
    font-weight: 700;
    font-size: 50px;
    line-height: 56px;
    letter-spacing: 2px;
    color: var(--brand-gold);
  }
  .brand__name {
    margin-top: 18px;
    font-weight: 700;
    font-size: 30px;
    line-height: 34px;
    letter-spacing: 4px;
    color: var(--brand-gold);
  }
  .brand__tagline {
    margin-top: 8px;
    font-weight: 700;
    font-size: 17px;
    line-height: 20px;
    letter-spacing: 2px;
    color: var(--brand-gold);
  }
  .brand__rule { width: 310px; height: 1px; background: var(--rule-light); margin: 28px 0 10px; }
  .brand__concepts {
    font-weight: 700;
    font-size: 13.5px;
    line-height: 18px;
    color: var(--muted-light);
    text-transform: uppercase;
    letter-spacing: 0.2px;
  }
  .brand__concepts .sep { padding: 0 5px; }
</style>
</head>
<body>
  <section class="card card--contact">
    <h1 class="contact__name">DANIEL HARPER</h1>
    <p class="contact__title">Managing Director</p>
    <div class="contact__rule"></div>
    <p class="contact__lines">
      <b>P:</b> 044-123 456 789<br>
      <b>M:</b> 044-123 456 789<br>
      <b>E:</b> info@webname.com<br>
      <b>W:</b> www.websitename.com
    </p>
    <div class="contact__rule contact__rule--lower"></div>
    <p class="contact__address">12345, Address Goes Here<br>Country Name, 123456.</p>
  </section>

  <section class="card card--brand">
    <div class="brand__mark">PWR</div>
    <div class="brand__name">PRAIRIE WEST</div>
    <div class="brand__tagline">RESTAURANT GROUP</div>
    <div class="brand__rule"></div>
    <p class="brand__concepts">
      Copperleaf Alehouse<span class="sep">|</span>Bramble Alehouse<br>
      Hollister's Wood Fired Grill<span class="sep">|</span>Fenwick Patty Company
    </p>
  </section>
</body>
</html>
```